Stationery for consulting company
Strategic Thinking. Inclusive Solutions. Measurable Impact
Project: Stationery for consulting company
Business Cards and Stationery
Professional
Benedo Ofurame Phd
Senior Partner
Plot 9 Umoru Close Oregun, Ikeja Lagos - Nigeria
Benedo.ofura@velmarq.com
www.velmarq.com
fdsfdffdsd

```html
<!DOCTYPE html>
<html lang="en">
<head>
<meta charset="utf-8">
<title>Velmarq Consulting — Business Card</title>
<link rel="stylesheet" href="https://fonts.googleapis.com/css2?family=Roboto:wght@400;700&family=Zilla+Slab:wght@700&display=swap">
<style>
  :root {
    --bg: #e4e5e6;
    --copper-dark: #b4541f;
    --copper: #cf6a2e;
    --gold: #d9a15a;
    --green: #1f5a35;
    --green-dark: #17462a;
    --orange: #e0662a;
    --ink: #6d6d6d;
    --rule: #c9c9c9;
    --card: #ffffff;
    --watermark: #f1f1f1;
  }
  * { box-sizing: border-box; margin: 0; padding: 0; }
  html, body { width: 1200px; height: 901px; overflow: hidden; }
  body {
    background: var(--bg);
    font-family: "Roboto", Arial, sans-serif;
    position: relative;
  }
  .card {
    position: absolute;
    left: 300px;
    width: 600px;
    height: 360px;
    border-radius: 16px;
    overflow: hidden;
  }
  .card-back {
    top: 70px;
    background: linear-gradient(125deg, var(--gold) 0%, var(--copper) 35%, var(--copper-dark) 65%, var(--copper) 100%);
  }
  .card-front {
    top: 472px;
    background: var(--card);
  }
  .watermark {
    position: absolute;
    right: -40px;
    top: 40px;
    width: 300px;
    height: 300px;
    border-radius: 50%;
    background: var(--watermark);
  }
  .brand {
    position: absolute;
    left: 24px;
    top: 28px;
    display: flex;
    align-items: center;
    gap: 10px;
  }
  .brand-dot {
    width: 34px;
    height: 34px;
    border-radius: 50%;
    background: var(--orange);
  }
  .brand-name {
    font-weight: 700;
    font-size: 30px;
    letter-spacing: 1px;
    color: var(--green);
  }
  .person {
    position: absolute;
    left: 24px;
    top: 196px;
  }
  .person-name {
    font-family: "Zilla Slab", Georgia, serif;
    font-weight: 700;
    font-size: 29px;
    color: var(--green);
    line-height: 1;
  }
  .person-role {
    margin-top: 6px;
    font-size: 11px;
    color: var(--ink);
  }
  .divider {
    position: absolute;
    left: 24px;
    right: 24px;
    top: 254px;
    height: 1px;
    background: var(--rule);
  }
  .contacts {
    position: absolute;
    left: 24px;
    top: 276px;
    font-size: 12px;
    color: var(--ink);
    line-height: 17px;
  }
  .contact { display: flex; align-items: center; gap: 8px; }
  .contact svg { width: 10px; height: 10px; fill: var(--orange); }
  .address {
    position: absolute;
    right: 24px;
    top: 276px;
    font-size: 12px;
    color: var(--ink);
    line-height: 17px;
    text-align: right;
  }
  .footer-band {
    position: absolute;
    left: 0;
    bottom: 0;
    width: 600px;
    height: 40px;
  }
  .website {
    position: absolute;
    right: 28px;
    bottom: 10px;
    font-size: 12px;
    color: #ffffff;
  }
</style>
</head>
<body>
  <div class="card card-back" role="img" aria-label="Copper and gold foil pattern of repeated brand marks"></div>

  <div class="card card-front">
    <div class="watermark"></div>

    <div class="brand">
      <span class="brand-dot"></span>
      <span class="brand-name">VELMARQ</span>
    </div>

    <div class="person">
      <div class="person-name">Benedo Ofurame Phd</div>
      <div class="person-role">Senior Partner</div>
    </div>

    <div class="divider"></div>

    <div class="contacts">
      <div class="contact">
        <svg viewBox="0 0 10 10"><path d="M2 0.5 L3.8 2.6 L2.9 3.7 Q4 6 6.3 7.1 L7.4 6.2 L9.5 8 L8.3 9.5 Q3.5 9 0.5 1.7 Z"/></svg>
        <span>+234 (0) 805 417 3920</span>
      </div>
      <div class="contact">
        <svg viewBox="0 0 10 10"><rect x="0" y="2" width="10" height="6.5" rx="0.8"/></svg>
        <span>Benedo.ofura@velmarq.com</span>
      </div>
    </div>

    <div class="address">
      <div>Plot 9 Umoru Close Oregun</div>
      <div>Ikeja Lagos - Nigeria</div>
    </div>

    <svg class="footer-band" viewBox="0 0 600 40" preserveAspectRatio="none">
      <rect x="0" y="34" width="600" height="6" fill="var(--orange)"/>
      <polygon points="400,12 600,12 600,40 386,40" fill="var(--green-dark)"/>
    </svg>
    <div class="website">www.velmarq.com</div>
  </div>
</body>
</html>
```